new customer flyer 8.5 X 11 to get people who use CPAP, Snore or have sleep apnea to call us

We sell CPAP equipment and supplies in Ontario. We are designing a flyer for a an advertising campaign encouraging people to switch from the current CPAP supplier to us. Our company name is Breathwell Depot. We are different from a typical CPAP supply store in many ways. A typical store is open 9-5 monday-friday, and the customer must come to the store to get any service. We offer free delivery of supplies of the customer is using the same supplies, so they can just have their supplies shipped rather than come in to pick them up. We also offer free home visits where we will do all the services that can be done in store, including determine the best machine they need, fit them for a mask, set up their equipment and supplies, offer advice, and much more. We also offer night and weekend appointments. Finally we will buy used equipment from our customers and donate this equipment to those in the community who may not be able to afford new equipment, which has 2 benefits of reducing waste and helping the needy.

If you can come up with any other concepts to make us stand out we are open to this.

Our flyer needs to offer a call to action of providing a Prixa Gift card to new customers plus additional call to actions if you are able to create one based on info herein. The gift card amount is $50.00 if this is relevant. We can limit the number available for the promotion if you feel it would encourage a faster and quicker response rate.

The Info needed in the flyer is:
1) Company Name: Breathwell Depot
2) Phone number: 289-517-3064
3) website: www.breathwelldepot-example.com (Make creative in a way that it is easy for user to determine what it says and stimulate them to remember it.)
4) Address is optional, which is 418 Marlow Street, Fort Erie ON L2A 7K3
5) We cover the entire Niagara region and Region of Hamilton in Ontario Canada
6) A call to action is a MUST. We were thinking of using a $50 Prixa gift card for new customers or something else if you feel it would drive more calls to us or more website visits.
7) The objective is to get the customer to call us so we can make them a new customer. The secondary objective is to get the customer to visit our website, because even if they are hesitant to call us, we hope to get them to visit our website and this will give them the confidence to call us.
8) The call to action must encourage a response to hopefully get a call right away. we don't want the customer putting us on the back burner.
9) The flyer is encouraged to not only get people who have sleep apnea, snoring or are currently on CPAP to call, but to also get people who may not suffer from any of these conditions to want to give the flyer to their friends or family who does.
10) I included a bunch of pictures but they are just random pictures, you can use them, use your own or use drawings or whatever to get the message across. You do not need to use all or any of the pictures I provided.
11) We accept all health insurances

I am pretty open, so have fun with the project and be creative as possible!
Updates

There are many designs submitted but many that do not meet the requirements, and many that are similar. I am hoping to find one that does not look like every other generic design, and work with some of the designers who have submitted entries with some potential to modify them into something useable.

Target Market(s)

1) People who snore, have sleep apnea or already use CPAP.
2) Spouses of people snore or have sleep apnea, as these people notice the person who is snoring or having erratic breathing.
3) Friends or family of the people above so that they share the flyer.
4) Focus on 30-60 year old males.

Industry/Entity Type

Advertising

Colors

Designer to choose colors to be used in the design.

Requirements
Must have
• 1) Company Name: Breathwell Depot (Logo can serve as company name as well, files attached)
• 2) Phone number: 289-517-3064
• 3) website: www.breathwelldepot-example.com (Make creative in a way that it is easy for user to determine what it says and stimulate them to remember it.)
• 4) Flyer needs to be friendly and engaging.
• 5) Flyer can be funny or humorous if it will generate customers.
• 6) A call to action is a MUST. We were thinking of using a $50 Prixa gift card for new customers or something else if you feel it would drive more calls to us or more website visits.
• 7) The objective is to get the customer to call us so we can make them a new customer. The secondary objective is to get the customer to visit our website, because even if they are hesitant to call us, we hope to get them to visit our website and this will give them the confidence to call us.
• 8) The call to action must encourage a response to hopefully get a call right away. we don't want the customer putting us on the back burner.
• 9) The flyer is encouraged to not only get people who have sleep apnea, snoring or are currently on CPAP to call, but to also get people who may not suffer from any of these conditions to want to give the flyer to their friends or family who does.
• 10) I included a bunch of pictures but they are just random pictures, you can use them, use your own or use drawings or whatever to get the message across. You do not need to use all or any of the pictures I provided.
• 11) We accept all health insurances
• 12) The FLYER MUST be bold and stand out. This can be with full color, unique text or graphics, or colored backgrounds (Including really bold colors). The point is there is really not a defined market to target with this industry, so any flyers are random location flyers that must be so bold as to grab someones attention such that they want to see what the flyer says.
• 13) Because CPAP only affects about 10-15% of the population, the flyer should be designed that those who snore, suffer from sleep apnea, or CURRENTLY USE CPAP will immediately relate to the flyer and as such want to read it and hopefully call us.
Nice to have
• 1) Address is optional, which is 418 Marlow Street, Fort Erie ON L2A 7K3 (We encourage people to let us come to them, because we offer free shipping and home visits. Therefore our address is not really terribly important.
• 2) We cover the entire Niagara region and Region of Hamilton in Ontario Canada. If they get our flyer they hopefully will call us, however if this can be fit in it confirms that we service the customers area. Without it the customer may wonder if we go to the area where they live.
• 3) Our Taglines are "We make CPAP Personal" and "Better sleep for better health", if they fit into the theme of the designed flyer feel free to add one or both of these.
• 4) The flyer can be designed to appear medical in design if this works, but I prefer fun, engaging and even humorous first, and the medical part becomes secondayry.
Should not have
• 1) The flyer can not be scary or make someone feel uncomfortable.

```html
<!DOCTYPE html>
<html lang="en">
<head>
<meta charset="utf-8">
<title>Breathwell Depot – New Customer Flyer</title>
<link rel="stylesheet" href="https://fonts.googleapis.com/css2?family=Jost:wght@400;500;700&family=Open+Sans:ital,wght@0,400;0,600;0,700;1,400;1,600&display=swap">
<style>
  :root{
    --purple:#8c55a8;
    --purple-dark:#5d3f6c;
    --purple-band:#8b52a6;
    --green:#2aa464;
    --row-light:#f3eff3;
    --row-dark:#e9e4eb;
    --ink:#3a3140;
    --ink-soft:#4a4450;
    --ribbon:#d8241f;
    --white:#ffffff;
  }
  *{box-sizing:border-box;margin:0;padding:0}
  html,body{width:934px;height:1200px;overflow:hidden;background:#fff}
  .flyer{position:relative;width:934px;height:1200px;overflow:hidden;background:var(--row-light);font-family:"Jost",sans-serif;color:var(--ink)}

  .hero{position:absolute;left:0;top:0;width:934px;height:600px}
  .hero-photo{position:absolute;inset:0;
    background:
      linear-gradient(100deg, rgba(255,255,255,0) 62%, rgba(222,196,160,.85) 80%, #e2c9a4 100%),
      radial-gradient(ellipse at 45% 40%, #c9cfe0 0%, #e9ebf1 35%, #f7f7f9 60%, #eeeeef 100%);}
  .hero-wave{position:absolute;left:0;top:0}

  .brand{position:absolute;left:52px;top:86px;display:flex;align-items:center;gap:8px;
    font-family:"Open Sans",sans-serif;font-weight:400;font-size:25px;color:var(--green);letter-spacing:-.2px}
  .brand-dot{width:10px;height:10px;border-radius:50%;background:var(--purple)}

  .tagline{position:absolute;right:46px;top:308px;font-family:"Open Sans",sans-serif;font-style:italic;font-weight:600;font-size:14.5px;color:#4b4150}

  .pill{position:absolute;right:36px;height:39px;border-radius:20px;background:var(--purple);
    display:flex;align-items:center;justify-content:space-between;padding-left:26px;padding-right:2px;
    font-family:"Open Sans",sans-serif;font-weight:700;font-size:14.5px;letter-spacing:.6px;color:var(--white)}
  .pill.delivery{top:346px;width:238px}
  .pill.visits{top:400px;width:212px}
  .pill-icon{width:35px;height:35px;border-radius:50%;background:var(--green);border:2px solid #fff;display:flex;align-items:center;justify-content:center;margin-left:12px}

  .benefits{position:absolute;left:0;top:552px;width:934px}
  .benefit{padding:0 78px}
  .benefit.alt{background:var(--row-dark)}
  .benefit h2{font-family:"Jost",sans-serif;font-weight:700;font-size:15.5px;letter-spacing:.3px;color:#3b3342;text-transform:uppercase}
  .benefit p{font-size:14.4px;line-height:21.5px;color:var(--ink-soft);margin-top:8px}
  .b1{height:70px;padding-top:12px}
  .b2{height:94px;padding-top:13px}
  .b3{height:94px;padding-top:12px}
  .b4{height:118px;padding-top:13px}

  .contact{position:absolute;left:75px;top:950px;font-family:"Open Sans",sans-serif;font-weight:700;color:var(--purple)}
  .contact-row{display:flex;align-items:center;height:44px}
  .contact-label{width:223px;font-size:24px;letter-spacing:.4px}
  .contact-icon{width:21px;height:21px;border-radius:50%;background:var(--purple);display:flex;align-items:center;justify-content:center;margin-right:8px}
  .contact-value{font-size:24px;letter-spacing:1.4px}

  .offer{position:absolute;left:0;top:1058px;width:934px;height:142px}
  .offer-shapes{position:absolute;left:0;top:0}
  .offer-limited{position:absolute;left:46px;top:18px;font-family:"Open Sans",sans-serif;font-style:italic;font-size:16.5px;color:var(--white);letter-spacing:.3px}
  .offer-card{position:absolute;left:46px;top:78px;font-family:"Open Sans",sans-serif;color:var(--white)}
  .offer-card strong{display:block;font-weight:700;font-size:16.5px;letter-spacing:.5px}
  .offer-card span{display:block;font-size:16.5px;letter-spacing:.4px;margin-top:3px}
  .insurance{position:absolute;right:39px;top:17px;font-family:"Open Sans",sans-serif;font-size:16.5px;color:#3e3a44;letter-spacing:.2px}
  .coverage{position:absolute;right:39px;top:68px;text-align:right;font-family:"Open Sans",sans-serif;font-size:16.5px;line-height:24px;color:#3e3a44;letter-spacing:.2px}
</style>
</head>
<body>
<main class="flyer">

  <section class="hero">
    <div class="hero-photo" role="img" aria-label="Photo of a smiling couple relaxing in bed, the man wearing a nasal CPAP mask and looking at a tablet"></div>
    <svg class="hero-wave" width="934" height="600" viewBox="0 0 934 600" aria-hidden="true">
      <path d="M0,588 C40,528 80,498 160,496 C260,494 300,543 380,546 C460,549 540,488 640,486 C740,484 820,538 934,550 L934,600 L0,600 Z" fill="var(--purple)"/>
      <path d="M0,598 C40,540 80,508 160,506 C260,504 300,553 380,556 C460,559 540,498 640,496 C740,494 820,548 934,560 L934,600 L0,600 Z" fill="var(--row-light)"/>
    </svg>

    <div class="brand"><span class="brand-dot"></span>Breathwell Depot</div>

    <p class="tagline">“We make CPAP personal”</p>

    <div class="pill delivery">FREE HOME DELIVERY
      <span class="pill-icon"><svg width="18" height="14" viewBox="0 0 18 14" aria-hidden="true"><rect x="1" y="2" width="10" height="8" fill="#fff"/><path d="M11 5h4l2 3v2h-6z" fill="#fff"/><circle cx="4" cy="11.5" r="1.8" fill="#fff"/><circle cx="14" cy="11.5" r="1.8" fill="#fff"/></svg></span>
    </div>
    <div class="pill visits">FREE HOME VISITS
      <span class="pill-icon"><svg width="16" height="16" viewBox="0 0 16 16" aria-hidden="true"><path d="M8 1 L15 7 H13 V15 H3 V7 H1 Z" fill="#fff"/><rect x="6.5" y="10" width="3" height="5" fill="var(--green)"/></svg></span>
    </div>
  </section>

  <section class="benefits">
    <article class="benefit b1">
      <h2>Free Delivery</h2>
      <p>So you can spend your time off doing the things you love.</p>
    </article>
    <article class="benefit b2 alt">
      <h2>Free Home Visits</h2>
      <p>Because we don't just want to sell you supplies, we want to set them up for you, make sure all your questions are answered, and make sure you get everything you need.</p>
    </article>
    <article class="benefit b3">
      <h2>Night and Weekend Appointments</h2>
      <p>Not everyone works 9-5 Monday through Friday.&nbsp; We offer night and weekend appointments to make sure you can get the service you need on your schedule.</p>
    </article>
    <article class="benefit b4 alt">
      <h2>We Buy Your Old Supplies</h2>
      <p>There are many people who can't afford their supplies, but we want to help them however we can. So part of our commitment to serving everyone is that we buy your gently used equipment, refurbish what we can, and donate it to those who need it.</p>
    </article>
  </section>

  <section class="contact">
    <div class="contact-row">
      <span class="contact-label">Call us today:</span>
      <span class="contact-icon"><svg width="12" height="12" viewBox="0 0 12 12" aria-hidden="true"><path d="M2.5 1 L4.5 1 L5.2 3.6 L4 4.6 C4.6 6 6 7.4 7.4 8 L8.4 6.8 L11 7.5 L11 9.5 C11 10.3 10.3 11 9.5 11 C5 11 1 7 1 2.5 C1 1.7 1.7 1 2.5 1Z" fill="#fff"/></svg></span>
      <span class="contact-value">(289) 517 3064</span>
    </div>
    <div class="contact-row">
      <span class="contact-label">Find us online:</span>
      <span class="contact-icon"><svg width="13" height="13" viewBox="0 0 13 13" aria-hidden="true"><g fill="none" stroke="#fff" stroke-width="1"><circle cx="6.5" cy="6.5" r="5"/><ellipse cx="6.5" cy="6.5" rx="2.2" ry="5"/><path d="M1.5 6.5h10M2.3 4h8.4M2.3 9h8.4"/></g></svg></span>
      <span class="contact-value">www.breathwelldepot-example.com</span>
    </div>
  </section>

  <section class="offer">
    <svg class="offer-shapes" width="934" height="142" viewBox="0 0 934 142" aria-hidden="true">
      <rect x="0" y="0" width="934" height="142" fill="var(--row-dark)"/>
      <line x1="570" y1="51" x2="934" y2="51" stroke="#d6d0d9" stroke-width="1"/>
      <polygon points="0,51 436,51 566,142 0,142" fill="var(--purple-band)"/>
      <polygon points="0,0 356,0 436,51 0,51" fill="var(--purple-dark)"/>
      <line x1="306" y1="0" x2="530" y2="142" stroke="var(--ribbon)" stroke-width="7"/>
    </svg>
    <p class="offer-limited">For a limited time only</p>
    <div class="offer-card">
      <strong>$50 Prixa Gift Card for New Customers</strong>
      <span>Call us for more information</span>
    </div>
    <p class="insurance">We accept all health insurances</p>
    <p class="coverage">We cover the entire Niagara region and<br>Region of Hamilton in Ontario Canada</p>
  </section>

</main>
</body>
</html>
```